Business Card Design Project

We need a simple business card design that uses our current logo.
We need to have the current logo put into a high res format.
We need to have 1 card made with contact information.
We will supply the information for the 4 employees.
Industry/Entity Type
Business
Requirements
Must have
- The contact information is as follows:
Mark Dellweather
Producer/CEO
c. 555-210-0147
f. 555-260-0193
markd@lanternbay.example
Al Vostrand, CFO
c. 949-555-0162
f. 555-260-0193
alv@lanternbay.example
Peter Malvane, PR
c. 267-555-0128
f. 555-260-0193
pmalvane@lanternbay.example
Tim Garrowby, Producer
c. 949-555-0184
f. 555-260-0193
timg@lanternbay.example
The address for all cards is:
318 W Calle Norvento #2715, Harbor Vale, NV 92681

```html
<!DOCTYPE html>
<html lang="en">
<head>
<meta charset="utf-8">
<title>Lantern Bay Media – Business Card</title>
<link rel="stylesheet" href="https://fonts.googleapis.com/css2?family=Open+Sans:wght@400;600;700&display=swap">
<style>
  :root {
    --stage: #3a3a3c;
    --card-dark: #1c1e22;
    --card-dark-edge: #2a2d33;
    --card-light: #f4f5f6;
    --card-light-fade: #e6e9ec;
    --accent-blue: #2a9fe0;
    --logo-blue: #5cb8ea;
    --ink: #2b2b2b;
  }
  * { box-sizing: border-box; margin: 0; padding: 0; }
  html, body {
    width: 1200px;
    height: 900px;
    overflow: hidden;
    background: var(--stage);
    font-family: "Open Sans", Arial, sans-serif;
  }
  .canvas {
    width: 1200px;
    height: 900px;
    display: flex;
    flex-direction: column;
    align-items: center;
    justify-content: center;
    gap: 60px;
  }
  .card {
    width: 630px;
    height: 360px;
    border-radius: 4px;
    position: relative;
    overflow: hidden;
    box-shadow: 0 10px 30px rgba(0, 0, 0, 0.45);
  }

  .card--back {
    background: radial-gradient(ellipse at 50% 45%, var(--card-dark-edge), var(--card-dark) 75%);
    display: flex;
    align-items: center;
    justify-content: center;
  }
  .card--back .company-name {
    font-size: 52px;
    font-weight: 700;
    color: var(--logo-blue);
    letter-spacing: 1px;
    text-transform: uppercase;
  }

  .card--front {
    background: linear-gradient(160deg, var(--card-light) 0%, var(--card-light) 55%, var(--card-light-fade) 100%);
  }
  .card--front .company-name {
    position: absolute;
    top: 30px;
    right: 38px;
    font-size: 36px;
    font-weight: 700;
    color: var(--logo-blue);
    text-transform: uppercase;
    letter-spacing: 0.5px;
  }
  .contact {
    position: absolute;
    left: 40px;
    top: 100px;
    color: var(--ink);
    font-size: 14px;
    line-height: 1.5;
  }
  .contact__name {
    font-size: 21px;
    font-weight: 400;
    color: var(--accent-blue);
    text-transform: uppercase;
    letter-spacing: 0.5px;
    line-height: 1.2;
  }
  .contact__title {
    font-size: 13px;
    margin-bottom: 14px;
  }
  .contact__label {
    color: var(--accent-blue);
    margin-right: 4px;
  }
  .address {
    position: absolute;
    left: 40px;
    bottom: 34px;
    font-size: 14px;
    color: var(--ink);
  }
</style>
</head>
<body>
  <main class="canvas">
    <section class="card card--back" aria-label="Card back">
      <span class="company-name">Lantern Bay Media</span>
    </section>

    <section class="card card--front" aria-label="Card front">
      <span class="company-name">Lantern Bay Media</span>
      <div class="contact">
        <p class="contact__name">Mark Dellweather</p>
        <p class="contact__title">Producer/CEO</p>
        <p><span class="contact__label">c.</span>555-210-0147</p>
        <p><span class="contact__label">f.</span>555-260-0193</p>
        <p><span class="contact__label">e.</span>markd@lanternbay.example</p>
      </div>
      <p class="address">318 W Calle Norvento #2715, Harbor Vale, NV 92681</p>
    </section>
  </main>
</body>
</html>
```